Flyer for American Indian Elders on Dementia Warning Signs

We need a flyer designed for older adults who are American Indian or Alaska Native (in the U.S.).

Ideally, the flyer should complement the colors of our logos. The project logo and our organization logo are attached to the brief.

When people see the flyer we want them to feel that it represents their culture, is warm, and professional but relatable to older adults and people who have limited incomes.

I have attached an earlier draft of the document we designed ourselves BUT we want different and better.

It is for older adults who have trouble reading so:
1. you must use a font that is 11.5 points or larger
2. Do not put text over complex pictures or use shading with words
3. You can use a serif font for the heading, but should use san serif for the body text
4. There should be good contrast between the font color and background

Please do not use any images that include a head dress or pictures of American Indian people or things that are very traditional or "token" imagery.

We need to save a small space under the call out box/ somewhere on the flyer for other people to add their logo once they download.

Let us know if you have questions or need additional information.

Target Market(s)

Older American Indian people

Font styles to use
Serif
Sans Serif

Requirements
Must have
• Easy to read for older adults
Should not have
• indian headdress

```html
<!DOCTYPE html>
<html lang="en">
<head>
<meta charset="utf-8">
<title>10 Signs of Thinking or Memory Changes That Might Be Dementia</title>
<link href="https://fonts.googleapis.com/css2?family=Barlow+Semi+Condensed:wght@700&family=Crimson+Pro:wght@700&family=Poppins:wght@400;600&display=swap" rel="stylesheet">
<style>
  :root {
    --red: #963a32;
    --teal: #2f8d96;
    --grey: #c6c8c7;
    --green: #5b9f3b;
    --leaf: #8cbf78;
    --ink: #1e1e1e;
    --panel-dark: #2b2b29;
    --white: #ffffff;
  }
  html, body { margin: 0; padding: 0; overflow: hidden; }
  body { width: 927px; height: 1200px; background: var(--grey); }
  .flyer {
    position: relative; width: 927px; height: 1200px; overflow: hidden;
    font-family: "Poppins", sans-serif; color: var(--ink);
  }
  .backdrop { position: absolute; inset: 0; }
  .sheet {
    position: absolute; left: 33px; top: 33px; width: 861px; height: 1133px;
    background: var(--white);
  }
  .title-block {
    position: absolute; left: 44px; top: 38px; width: 675px; height: 228px;
    background: var(--red); border-radius: 0 0 26px 26px;
  }
  .title-line {
    position: absolute; left: 8px; margin: 0; white-space: nowrap;
    font-family: "Crimson Pro", serif; font-weight: 700; color: var(--white);
    transform-origin: left top; line-height: 1;
  }
  .title-line.small { top: 8px; font-size: 38px; transform: scaleX(0.74); }
  .title-line.large { top: 40px; font-size: 62px; transform: scaleX(0.73); }
  .intro {
    position: absolute; left: 11px; top: 94px; width: 654px; height: 122px;
    background: var(--white); border-radius: 0 0 20px 20px; box-sizing: border-box;
    padding: 5px 8px 0 8px; font-size: 14.2px; line-height: 22.5px; letter-spacing: -0.3px;
  }
  .intro p { margin: 0; }
  .intro strong {
    font-family: "Barlow Semi Condensed", sans-serif; font-weight: 700;
    font-size: 15.6px; letter-spacing: 0;
  }
  .feathers {
    position: absolute; left: 732px; top: 42px; width: 156px; height: 236px;
    background: linear-gradient(100deg, #8fd0d6 0%, #8fd0d6 30%, #8cc77a 40%, #8cc77a 65%, #cf7a72 75%, #cf7a72 100%);
    opacity: 0.55; border-radius: 60px 60px 20px 20px;
  }
  .sign { position: absolute; left: 44px; width: 530px; }
  .sign-number {
    position: absolute; left: 0; top: 0; bottom: 0; width: 21px; background: var(--red);
    color: var(--white); font-family: "Barlow Semi Condensed", sans-serif; font-weight: 700;
    font-size: 24px; text-align: center; line-height: 1; padding-top: 4px; box-sizing: border-box;
  }
  .sign-number.double { font-size: 20px; letter-spacing: -2px; padding-top: 8px; }
  .sign-text {
    margin: 0 0 0 29px; font-size: 15px; line-height: 23.7px; letter-spacing: -0.3px;
  }
  .sign-lead {
    font-family: "Barlow Semi Condensed", sans-serif; font-weight: 700;
    font-size: 17px; letter-spacing: 0.1px;
  }
  .partner {
    position: absolute; display: flex; align-items: center; gap: 10px;
    font-family: "Poppins", sans-serif; font-weight: 600; line-height: 1.1;
  }
  .partner-mark { flex: none; border-radius: 50%; }
  .partner.project { left: 590px; top: 296px; width: 290px; color: var(--leaf); font-size: 20px; }
  .partner.project .partner-mark { width: 48px; height: 48px; background: var(--leaf); }
  .partner.center { left: 592px; top: 862px; width: 290px; color: var(--teal); font-size: 15px; }
  .partner.center .partner-mark { width: 70px; height: 70px; background: var(--teal); }
  .partner.council { left: 596px; top: 1036px; width: 286px; color: var(--red); font-size: 19px; }
  .partner.council .partner-mark { width: 52px; height: 52px; border-radius: 0; background: var(--teal); }
  .main-heading {
    position: absolute; left: 589px; top: 364px; width: 292px; margin: 0; text-align: center;
    font-family: "Crimson Pro", serif; font-weight: 700; font-size: 37px; color: var(--red);
    line-height: 1;
  }
  .main-points {
    position: absolute; left: 589px; top: 415px; width: 292px; height: 436px;
    background: var(--panel-dark); border-radius: 24px 0 24px 0; color: var(--white);
    box-sizing: border-box; padding: 8px 6px 0; text-align: center;
    font-size: 17.4px; line-height: 24.4px; letter-spacing: -0.3px;
  }
  .main-points p { margin: 0; }
  .point-divider {
    position: relative; height: 1px; background: var(--green); margin: 12px 12px 16px;
  }
  .point-divider::after {
    content: ""; position: absolute; left: 50%; top: -4px; width: 9px; height: 9px;
    margin-left: -4.5px; border-radius: 50%; background: var(--green);
  }
  .links {
    position: absolute; left: 608px; top: 952px; width: 272px; margin: 0; padding: 0; list-style: none;
    font-size: 15px; line-height: 23px; color: var(--ink); letter-spacing: -0.2px;
  }
  .links li { display: flex; align-items: center; gap: 8px; white-space: nowrap; }
  .links svg { flex: none; }
  .logo-space {
    position: absolute; left: 45px; top: 1105px; width: 833px; height: 52px;
    border: 1px solid var(--ink); border-radius: 12px; box-sizing: border-box;
  }
</style>
</head>
<body>
<main class="flyer">
  <svg class="backdrop" width="927" height="1200" viewBox="0 0 927 1200" aria-hidden="true">
    <rect width="927" height="1200" fill="var(--grey)"/>
    <polygon points="0,0 511,0 0,840" fill="var(--teal)"/>
    <polygon points="927,423 927,1200 456,1200" fill="var(--green)"/>
  </svg>
  <div class="sheet"></div>

  <header class="title-block">
    <h1 class="title-line small">10 SIGNS OF THINKING OR MEMORY CHANGES</h1>
    <h1 class="title-line large">THAT MIGHT BE DEMENTIA</h1>
    <div class="intro">
      <p>As you we get older, you we may slow down a bit. This is a normal part of aging. Changes in memory or thinking that make it harder to get through the day, are <u>not</u> a normal part of aging. These may be early signs of dementia. Because American Indian and Alaska Native people have a high risk of dementia, it is important to know the warning signs.</p>
      <p><strong>DO YOU HAVE ANY OF THESE 10 WARNING SIGNS? IF SO, TALK TO YOUR DOCTOR.</strong></p>
    </div>
  </header>

  <div class="feathers" role="img" aria-label="Illustration of three feathers in teal, green and red"></div>

  <section class="signs">
    <div class="sign" style="top:277px;height:66px"><div class="sign-number">1</div>
      <p class="sign-text"><span class="sign-lead">MEMORY LOSS THAT AFFECTS YOUR DAILY LIFE. YOU MAY:</span> Forget events or important dates, Repeat yourself, Rely more often on lists or sticky notes to remember things.</p></div>
    <div class="sign" style="top:360px;height:64px"><div class="sign-number">2</div>
      <p class="sign-text"><span class="sign-lead">TROUBLE PLANNING OR SOLVING PROBLEMS. YOU MAY HAVE A HARDER TIME:</span> Paying bills, Cooking recipes you have used for years.</p></div>
    <div class="sign" style="top:443px;height:45px"><div class="sign-number">3</div>
      <p class="sign-text"><span class="sign-lead">YOU GET GET CONFUSED ABOUT THE TIME, DATE, OR WHERE YOU ARE.</span></p></div>
    <div class="sign" style="top:503px;height:43px"><div class="sign-number">4</div>
      <p class="sign-text"><span class="sign-lead">DAILY TASKS ARE GETTING HARDER, INCLUDING:</span> Driving, Making a grocery list or going shopping.</p></div>
    <div class="sign" style="top:562px;height:68px"><div class="sign-number">5</div>
      <p class="sign-text"><span class="sign-lead">TROUBLE WITH HOW YOUR EYESIGHT AND THINKING WORK TOGETHER THAT GETS WORSE. THIS INCLUDES:</span> Tripping, falls, or problems with your balance, Spilling or dropping things more.</p></div>
    <div class="sign" style="top:646px;height:66px"><div class="sign-number">6</div>
      <p class="sign-text"><span class="sign-lead">NEW TROUBLE TALKING OR WRITING.</span> You have a hard time finding the words you want to say. For example, you may say “that thing on your wrist that tells time” instead of “watch.”</p></div>
    <div class="sign" style="top:729px;height:69px"><div class="sign-number">7</div>
      <p class="sign-text"><span class="sign-lead">YOU LOSE LOSE AND CANNOT FIND THINGS. FOR EXAMPLE, YOU:</span> Can't find the coffee pot that you use every day, Might put your car keys in the freezer.</p></div>
    <div class="sign" style="top:813px;height:66px"><div class="sign-number">8</div>
      <p class="sign-text"><span class="sign-lead">NOTICE CHANGES IN YOUR MOOD OR PERSONALITY, SUCH AS BEING:</span> Easily mad or sad in everyday situations, More fearful (scared) or suspicious (not trusting).</p></div>
    <div class="sign" style="top:896px;height:111px"><div class="sign-number">9</div>
      <p class="sign-text"><span class="sign-lead">ACT DIFFERENT AND ACT WITHOUT THINKING. MAKE POOR CHOICES. THIS MAY MAKE YOU MORE LIKELY TO:</span> Spend money you do not have or be a scam victim, Not Stop washing up regularly or pay less attention to how you look, Forget to take care of your pet</p></div>
    <div class="sign" style="top:1026px;height:69px"><div class="sign-number double">10</div>
      <p class="sign-text"><span class="sign-lead">PULL AWAY FROM FRIENDS AND FAMILY BECAUSE IT IS HARDER TO KEEP UP.</span> You may not want to do things you used to enjoy, like sporting events, church, music, or sex.</p></div>
  </section>

  <div class="partner project"><span class="partner-mark"></span><span>CLEAR MIND PROJECT</span></div>

  <h2 class="main-heading">MAIN POINTS</h2>
  <aside class="main-points">
    <p>American Indian and Alaska Native people have a higher risk of dementia.</p>
    <div class="point-divider"></div>
    <p>Big changes in memory or thinking that make it hard to get through the day are not a normal part of aging.</p>
    <div class="point-divider"></div>
    <p>People with one or more of these 10 signs should talk to their doctor to find the cause. It is not always dementia.</p>
    <div class="point-divider"></div>
    <p>Early dementia diagnosis gives you a chance to get care and plan your future.</p>
  </aside>

  <div class="partner center"><span class="partner-mark"></span><span>NORTHERN CIRCLE BRAIN WELLNESS CENTER</span></div>

  <ul class="links">
    <li><svg width="14" height="14" viewBox="0 0 14 14" aria-hidden="true"><circle cx="7" cy="7" r="6" fill="none" stroke="var(--teal)" stroke-width="1.4"/><ellipse cx="7" cy="7" rx="2.6" ry="6" fill="none" stroke="var(--teal)" stroke-width="1"/><line x1="1" y1="7" x2="13" y2="7" stroke="var(--teal)" stroke-width="1"/></svg>www.circlebrainwellness.org</li>
    <li><svg width="14" height="14" viewBox="0 0 14 14" aria-hidden="true"><circle cx="7" cy="7" r="6" fill="none" stroke="var(--teal)" stroke-width="1.4"/><ellipse cx="7" cy="7" rx="2.6" ry="6" fill="none" stroke="var(--teal)" stroke-width="1"/><line x1="1" y1="7" x2="13" y2="7" stroke="var(--teal)" stroke-width="1"/></svg>www.elderhealthinfo.org/aging</li>
  </ul>

  <div class="partner council"><span class="partner-mark"></span><span>COUNCIL FOR ELDER WELLNESS</span></div>

  <div class="logo-space" aria-label="Space for a partner logo"></div>
</main>
</body>
</html>
```